Piano Tuning Company Needs a Postcard Design to Advertise Online Appointments

I need a postcard design for my piano tuning company. I help maintain my client's piano by tuning and doing minor repairs to increase the joy of playing their instrument. My website is now set up to book appointments online and I would like to offer $10 off of any service for making an appointment from our website, valid for 2014 only. The online booking application allows customers to see all openings on the calendar for the service they are looking for and sidesteps playing phone tag to set up an appointment. I would like to see designs that go well with the logo and its color scheme. The final design should communicate warmth, professionalism and a desire to maintain their beautiful instrument.

Target Market(s)

People who own pianos

Industry/Entity Type

It Company

Requirements
Must have
• lunaridgecrafts@brindlemail.net
• (425) 736-1905
• Try our online booking service and receive $10 off any service
• Offer only valid for 2014
Nice to have
• Definitely picture(s) of pianos. I have attached one that is also on my business card, but if a different picture(s) work better for your design, please feel free to use it.
• It might be nice to have something about "avoid playing phone tag, try our online service." Or there could be something about a piano needing to be tuned once a year, and when was the last time your piano was tuned?

```html
<!DOCTYPE html>
<html lang="en">
<head>
<meta charset="utf-8">
<title>Ridgeline Piano Care Postcard</title>
<link href="https://fonts.googleapis.com/css2?family=Lobster&family=Merriweather:wght@400;700&family=Open+Sans:wght@400&display=swap" rel="stylesheet">
<style>
:root{
  --backdrop:#6d7073;
  --paper:#ffffff;
  --ink:#1f1a1c;
  --plum:#6e2a70;
  --magenta:#e6168a;
  --night:#0b0b0b;
  --line:#9a9a9a;
}
*{margin:0;padding:0;box-sizing:border-box}
html,body{width:945px;height:1200px;overflow:hidden;background:var(--backdrop)}
.canvas{position:relative;width:945px;height:1200px}
.card{position:absolute;left:80px;width:785px;background:var(--paper);overflow:hidden}
.card--front{top:56px;height:506px}
.card--back{top:630px;height:505px}
.abs{position:absolute}
.serif{font-family:'Merriweather',Georgia,serif}
.script{font-family:'Lobster',cursive}

/* front */
.hero-photo{left:0;top:0;width:588px;height:349px;background:linear-gradient(160deg,#f4f4f4 0%,#d9d9d9 35%,#8a8a8a 60%,#2a2a2a 85%,#111 100%)}
.hero-dark{left:588px;top:0;width:197px;height:349px;background:var(--night)}
.headline{left:34px;top:42px;font-size:30px;line-height:36px;color:var(--ink)}
.headline span{display:block;padding-left:24px}
.mission{left:604px;top:122px;width:160px;font-size:14px;line-height:20.5px;color:#fff;font-weight:700}
.book-band{left:0;top:349px;width:785px;height:33px;background:var(--plum);color:#fff;font-size:18px;font-weight:700;line-height:33px;padding-left:50px;letter-spacing:.3px}
.offer-badge{left:587px;top:261px;width:162px;height:162px;border-radius:50%;background:var(--magenta);border:4px solid #fff;color:#fff;text-align:center;font-weight:700}
.offer-badge .offer-word{position:absolute;left:0;right:0;top:26px;font-size:24px}
.offer-badge .amount{position:absolute;left:26px;top:46px;font-size:60px;line-height:70px}
.offer-badge .off-word{position:absolute;left:82px;top:102px;font-size:22px}
.brand{left:62px;top:410px;display:flex;align-items:center;gap:12px}
.brand-dot{width:44px;height:44px;border-radius:50%;background:var(--plum)}
.brand-name{font-family:'Merriweather',Georgia,serif;font-size:28px;color:var(--plum);font-weight:400}
.offer-terms{left:540px;top:430px;width:236px;text-align:center;font-size:13.5px;line-height:19px;font-weight:700;color:var(--plum)}
.offer-terms .valid{color:var(--magenta)}

/* back */
.back-title{left:20px;top:22px;font-size:24px;color:var(--magenta)}
.hands-photo{left:0;top:63px;width:272px;height:149px;background:linear-gradient(135deg,#2b2b2b 0%,#8c8c8c 40%,#e2e2e2 60%,#555 100%)}
.services{left:272px;top:63px;width:204px;height:149px;background:var(--plum);color:#fff;padding:28px 0 0 17px}
.services h2{font-size:13.5px;font-weight:700;margin-bottom:10px}
.services li{list-style:none;font-size:14px;font-weight:700;line-height:26px}
.services li::before{content:"•";color:var(--magenta);margin-right:6px}
.owner-name{left:30px;top:230px;font-family:'Open Sans',Arial,sans-serif;font-size:18px;color:var(--ink);letter-spacing:.3px}
.owner-bio{left:28px;top:268px;width:270px;font-size:10.6px;line-height:13.8px;color:var(--ink)}
.portrait{left:317px;top:213px;width:159px;height:142px;background:linear-gradient(180deg,#a23b56 0%,#b79c84 50%,#7d3a4e 100%)}
.contact{left:0;top:356px;width:315px;height:80px;background:var(--magenta);color:#fff;padding:8px 0 0 29px}
.contact .phone{font-size:18px;font-weight:700;line-height:24px}
.contact .line{font-size:12.5px;line-height:18px}
.brand--small{left:330px;top:380px;gap:6px}
.brand--small .brand-dot{width:20px;height:20px}
.brand--small .brand-name{font-size:13px}
.return-address{left:487px;top:60px;font-size:10px;line-height:15px;color:var(--ink)}
.return-address strong{display:block}
.stamp-box{left:675px;top:28px;width:83px;height:92px;border:1px solid #888}
.address-line{left:558px;width:193px;height:1px;background:var(--line)}
</style>
</head>
<body>
<div class="canvas">

  <section class="card card--front">
    <div class="abs hero-photo" role="img" aria-label="Close-up photo of a white grand piano keyboard"></div>
    <div class="abs hero-dark"></div>
    <h1 class="abs headline script">Your Piano should<span>Look, Play and Sound Beautiful.</span></h1>
    <p class="abs mission serif">Maintaing Piano by tuning and doing minor repairs to increase the joy of playing their instrument.</p>
    <div class="abs book-band serif">BOOK&nbsp; APPOINTMENTS ONLINE NOW !!</div>
    <div class="abs offer-badge serif">
      <span class="offer-word">OFFER</span>
      <span class="amount">$10</span>
      <span class="off-word">OFF</span>
    </div>
    <div class="abs brand"><span class="brand-dot"></span><span class="brand-name">Ridgeline Piano Care</span></div>
    <p class="abs offer-terms serif">Any service for making an appointment from our website<br><span class="valid">valid for 2014 only</span></p>
  </section>

  <section class="card card--back">
    <h2 class="abs back-title script">Enjoy Your Piano ......</h2>
    <div class="abs hands-photo" role="img" aria-label="Photo of hands playing a piano keyboard"></div>
    <div class="abs services serif">
      <h2>SERVICES OFFERED :</h2>
      <ul>
        <li>Standard Tuning</li>
        <li>Pitch Raise Plus Tuning</li>
        <li>All types of Repair</li>
      </ul>
    </div>
    <h3 class="abs owner-name">MARLA DENHOLT</h3>
    <p class="abs owner-bio serif">I’ve been playing the piano for over thirty years and all of my children play.&nbsp; As soon as one of the pianos is tuned in our home, everyone rediscovers the joy of playing.&nbsp; I would love to be a part of filling your home with beautiful music!</p>
    <div class="abs portrait" role="img" aria-label="Portrait photo of the piano tuner"></div>
    <div class="abs contact serif">
      <p class="phone">Call Now : (425) 736-1905</p>
      <p class="line">www.ridgelinepianocare.com</p>
      <p class="line">Email : lunaridgecrafts@brindlemail.net</p>
    </div>
    <div class="abs brand brand--small"><span class="brand-dot"></span><span class="brand-name">Ridgeline Piano Care</span></div>
    <p class="abs return-address serif"><strong>Ridgeline Piano Care</strong>Cedar Hollow,<br>Washington 98070</p>
    <div class="abs stamp-box"></div>
    <div class="abs address-line" style="top:244px"></div>
    <div class="abs address-line" style="top:295px"></div>
    <div class="abs address-line" style="top:342px"></div>
  </section>

</div>
</body>
</html>
```